Brit Rock covers band "The Tin Kettles" requires poster for Marlowe Lounge Friday March 31st

I want a design for a poster (A3 and A4) and Facebook/Instagram ads.
Primary focus is the band name logo "The Tin Kettles", style as in attached file, followed by tag "Old Skool Brit Rock".
Backdrop to be 60's psychedelic art.
Secondary focus is the venue "The Marlowe Lounge"
Supporting text to include:
- 27 Fenwick Road, Chatswood SYDNEY
- Friday 31st March 2023
- 7:00 pm until late
- Bar sales refreshments
- NO admission fee

```html
<!DOCTYPE html>
<html lang="en">
<head>
<meta charset="utf-8">
<title>The Tin Kettles – Old Skool Brit Rock</title>
<link rel="stylesheet" href="https://fonts.googleapis.com/css2?family=Arvo:wght@400;700&display=swap">
<style>
  :root {
    --page: #2e2e2e;
    --cream: #fffbc8;
    --orange: #e05326;
    --mint: #9fcbb0;
    --peach: #fedb9e;
    --olive: #7b7558;
    --ink: #000000;
    --logo-grey: #e4e4e4;
  }
  * { margin: 0; padding: 0; box-sizing: border-box; }
  html, body {
    width: 1200px; height: 1200px; overflow: hidden;
    background: var(--page);
    font-family: "Arvo", serif;
  }
  .poster {
    position: absolute; left: 197px; top: 30px;
    width: 806px; height: 1140px; overflow: hidden;
  }
  .backdrop {
    position: absolute; inset: 0;
    background:
      linear-gradient(125deg,
        var(--cream) 0%, var(--peach) 18%, var(--orange) 34%,
        var(--cream) 48%, var(--mint) 62%, var(--olive) 78%,
        var(--peach) 90%, var(--orange) 100%);
  }
  .body-shape {
    position: absolute; left: 22px; top: 0;
    width: 760px; height: 1104px;
    background: var(--ink);
    border-radius: 40% 40% 50% 50% / 26% 26% 44% 44%;
  }
  .line {
    position: absolute; left: 0; width: 774px;
    text-align: center; white-space: nowrap;
    color: var(--cream);
  }
  .band-name {
    top: 160px; font-size: 66px; line-height: 76px; font-weight: 700;
    color: var(--logo-grey); letter-spacing: -1px;
  }
  .tag-top { top: 360px; font-size: 54px; letter-spacing: 5px; }
  .tag-top .old { color: var(--mint); }
  .tag-brit { top: 410px; font-size: 142px; line-height: 150px; letter-spacing: 6px; }
  .tag-rock { top: 548px; font-size: 104px; line-height: 110px; letter-spacing: 10px; color: var(--orange); }
  .venue-label { top: 682px; font-size: 26px; }
  .venue-label span::before, .venue-label span::after {
    content: ""; display: inline-block; width: 34px; height: 1px;
    background: var(--orange); vertical-align: middle; margin: 0 4px;
  }
  .venue-name { top: 718px; font-size: 33px; color: var(--orange); }
  .rule {
    position: absolute; left: 367px; width: 40px; height: 2px;
    background: var(--mint);
  }
  .rule-a { top: 784px; }
  .rule-b { top: 959px; }
  .address { top: 810px; font-size: 18px; }
  .date { top: 845px; font-size: 36px; }
  .time { top: 895px; font-size: 36px; }
  .note-bar { top: 985px; font-size: 20px; }
  .note-fee { top: 1022px; font-size: 20px; }
</style>
</head>
<body>
  <main class="poster">
    <div class="backdrop" role="img" aria-label="Sixties psychedelic flowing stripe backdrop in cream, orange, mint, peach and olive"></div>
    <div class="body-shape" role="img" aria-label="Black electric guitar body silhouette"></div>

    <h1 class="line band-name">THE TIN<br>KETTLES</h1>

    <p class="line tag-top"><span class="old">OLD</span> SKOOL</p>
    <p class="line tag-brit">BRIT</p>
    <p class="line tag-rock">ROCK</p>

    <p class="line venue-label"><span>VENUE</span></p>
    <p class="line venue-name">THE MARLOWE LOUNGE</p>
    <div class="rule rule-a"></div>

    <p class="line address">27 FENWICK ROAD, CHATSWOOD SYDNEY</p>
    <p class="line date">FRIDAY 31ST MARCH 2023</p>
    <p class="line time">7:00 PM UNTIL LATE</p>
    <div class="rule rule-b"></div>

    <p class="line note-bar">BAR SALES REFRESHMENTS</p>
    <p class="line note-fee">NO ADMISSION FEE</p>
  </main>
</body>
</html>
```